Minimalist, Flat(Matte) design for a Beef Jerky packaging company. No bullshit company looking for a

Need a packaging design for a new Beef Jerky product(in English). The name of the company is 'Vellorn' and thus the packaging should reflect the bullish, tough, and simple nature of the beef jerky product. The finished product should communicate simplicity, minimalism, yet toughness and strength.

The logo should be simple, with a minimal number of colors , and should be either all white/cream, or have some red as well. Main colors should be white, cream, tinted red, and matte black. I think 4 colors max would be best. The closest example to an existing package style would be Kessip Noir clove cigarettes( image attached).

It will be on a matte black standing pouch package. See image for package type. Package dimensions:

Dimension: Width x Gusset x Height
INCH : 5.125" (W) x 3.125" (G) x 8.125" (H)
MILLIMETER : 130mm (W) x 80mm (G) x 205mm (H)

I don't have anything totally specific so artistic liberty is encouraged, provided the colors are kept to a minimum and looks consistent with the simple nature of the brand and the matte black packaging.

Also attached an existing beef jerky package with a similar style to what we're looking for.

Industry/Entity Type

It Company

Colors
f59195
ffffff

Requirements
Must have
• Low contrast, flat and minimalist design.
Should not have
• A complicated design with many colors. Gawdy/flashy design. Bright colors. High contrast.

```html
<!DOCTYPE html>
<html lang="en">
<head>
<meta charset="utf-8">
<title>Vellorn Beef Jerky – Pouch Labels</title>
<link rel="stylesheet" href="https://fonts.googleapis.com/css2?family=Archivo+Black&family=Oswald:wght@300;400;500;600&display=swap">
<style>
  :root {
    --matte-black: #000000;
    --paper: #ffffff;
    --cream: #f8dd8c;
    --tinted-red: #f5836f;
    --line-white: #ffffff;
  }
  html, body {
    margin: 0;
    padding: 0;
    width: 1200px;
    height: 930px;
    overflow: hidden;
    background: var(--paper);
  }
  .label-sheet { display: block; width: 1200px; height: 930px; }
  .pouch-face { fill: var(--matte-black); }
  .rule-white { stroke: var(--line-white); stroke-width: 4; fill: none; }
  .rule-cream { stroke: var(--cream); stroke-width: 4; fill: none; }
  .flavour-name {
    font-family: "Archivo Black", "Arial Black", sans-serif;
    fill: var(--cream);
    font-size: 96px;
  }
  .product-type {
    font-family: "Oswald", "Arial Narrow", sans-serif;
    font-weight: 300;
    fill: var(--paper);
    font-size: 128px;
  }
  .claims {
    font-family: "Oswald", "Arial Narrow", sans-serif;
    font-weight: 500;
    fill: var(--paper);
    font-size: 30px;
  }
  .net-weight {
    font-family: "Oswald", "Arial Narrow", sans-serif;
    font-weight: 400;
    fill: var(--paper);
    font-size: 30px;
  }
  .brand-name {
    font-family: "Oswald", "Arial Narrow", sans-serif;
    font-weight: 600;
    fill: var(--paper);
    font-size: 44px;
    letter-spacing: 2px;
  }
  .brand-dot { fill: var(--tinted-red); }
  .flavour-number-one { fill: var(--tinted-red); }
  .flavour-number-two {
    font-family: "Archivo Black", "Arial Black", sans-serif;
    fill: var(--paper);
    font-size: 240px;
  }
</style>
</head>
<body>
<svg class="label-sheet" viewBox="0 0 1200 930" xmlns="http://www.w3.org/2000/svg">

  <!-- Flavour 1: Original -->
  <g class="label label-original">
    <rect class="pouch-face" x="20" y="18" width="565" height="896"/>
    <line class="rule-white" x1="20" y1="191" x2="189" y2="18"/>
    <polygon class="rule-white" points="233,246 483,246 233,487"/>
    <line class="rule-white" x1="233" y1="246" x2="233" y2="914"/>
    <line class="rule-white" x1="20" y1="618" x2="585" y2="618"/>
    <line class="rule-white" x1="417" y1="846" x2="585" y2="846"/>

    <g class="brand-mark">
      <rect class="brand-dot" x="233" y="150" width="22" height="22"/>
      <text class="brand-name" x="264" y="176" textLength="150" lengthAdjust="spacingAndGlyphs">VELLORN</text>
    </g>

    <text class="flavour-name" transform="translate(187 580) rotate(-90)" textLength="396" lengthAdjust="spacingAndGlyphs">ORIGINAL</text>
    <text class="product-type" x="274" y="580" textLength="262" lengthAdjust="spacingAndGlyphs">beef jerky</text>

    <path class="flavour-number-one" d="M117 652 H177 a5 5 0 0 1 5 5 V824 a5 5 0 0 1 -5 5 H154 a5 5 0 0 1 -5 -5 V689 H117 a5 5 0 0 1 -5 -5 V657 a5 5 0 0 1 5 -5 Z"/>

    <text class="claims" x="275" y="668">ALL NATURAL</text>
    <text class="claims" x="275" y="702">HAND CRAFTED</text>
    <text class="claims" x="275" y="736">SMALL BATCH</text>
    <text class="net-weight" x="275" y="849" textLength="107" lengthAdjust="spacingAndGlyphs">NET WT. 3 OZ</text>
  </g>

  <!-- Flavour 2: Teriyaki -->
  <g class="label label-teriyaki">
    <rect class="pouch-face" x="617" y="18" width="564" height="896"/>
    <line class="rule-cream" x1="845" y1="58" x2="845" y2="851"/>
    <line class="rule-cream" x1="638" y1="618" x2="1157" y2="618"/>

    <g class="brand-mark">
      <circle class="brand-dot" cx="930" cy="225" r="12"/>
      <text class="brand-name" x="952" y="241" textLength="150" lengthAdjust="spacingAndGlyphs">VELLORN</text>
    </g>

    <text class="flavour-name" transform="translate(798 580) rotate(-90)" textLength="399" lengthAdjust="spacingAndGlyphs">TERIYAKI</text>
    <text class="product-type" x="869" y="580" textLength="262" lengthAdjust="spacingAndGlyphs">beef jerky</text>

    <text class="flavour-number-two" x="674" y="829" textLength="122" lengthAdjust="spacingAndGlyphs">2</text>

    <text class="claims" x="869" y="668">ALL NATURAL</text>
    <text class="claims" x="869" y="702">HAND CRAFTED</text>
    <text class="claims" x="869" y="736">SMALL BATCH</text>
    <text class="net-weight" x="869" y="849" textLength="107" lengthAdjust="spacingAndGlyphs">NET WT. 3 OZ</text>
  </g>
</svg>
</body>
</html>
```